Modern web-site for a game changer new health app!

We need a very clean UX / UI design for our company website that will be used to sell our brand to large corporations and their employees. If we find a good match, we'd need you to do the app design and some graphics for ongoing design needs.

For a first of its kind app developed at Pelbrook University, making licensed holistic medicine accessible to everyday people through access and curation by democratizing holistic health.

Please read the details attached thoroughly and reach out if you have any questions. Many thanks!
Updates

I've updated our requirements to make it easier, please review new details in the PDF shared. Many thanks!

Final brief refinement just uploaded, much has been simplified with very clear guidelines, please update and apply. thanks much!

Target Market(s)

corporate employees and large C level corporate leaders

Industry/Entity Type

wellness

Number of Pages Required

4 page

Font styles to use
Other font styles liked:
• We need website design now and app and socials after, hoping the designer we choose now can work with us on a regular basis going forward

Requirements
Must have
• clean, modern, minimal rich
Nice to have
• some added touches to give a custom feel
Should not have
• pictures, natural looking images or shapes

```html
<!DOCTYPE html>
<html lang="en">
<head>
<meta charset="utf-8">
<title>VEYLA — Wellness for Everyone</title>
<link href="https://fonts.googleapis.com/css2?family=Montserrat:wght@400;500;600&family=Plus+Jakarta+Sans:wght@500;600;700;800&family=IBM+Plex+Mono:wght@400;600&display=swap" rel="stylesheet">
<style>
:root{
  --ink:#1f1f1f;
  --hero:#7b7b7b;
  --cream:#fff6e1;
  --orange:#f8b42c;
  --line:#f6d7a8;
  --soon:#d7d7d7;
  --tile:#a9a9a9;
  --muted:#777;
  --white:#fff;
}
*{box-sizing:border-box;margin:0;padding:0}
html,body{width:1200px;height:3567px;overflow:hidden}
body{position:relative;background:var(--white);font-family:"IBM Plex Mono",monospace;color:var(--ink)}
.abs{position:absolute}
.center-text{text-align:center;left:0;width:1200px}

.hero{left:0;top:0;width:1200px;height:624px;background:var(--hero)}
.band{left:0;width:1200px;background:var(--cream)}
.brand{left:33px;top:28px;font:600 19px "Montserrat",sans-serif;color:var(--white)}
.nav{top:34px;font:400 11px "IBM Plex Mono",monospace;letter-spacing:1px;color:var(--white)}
.nav.active{text-decoration:underline}
.pill{display:flex;align-items:center;justify-content:center;border-radius:22px;font:400 11px "IBM Plex Mono",monospace;letter-spacing:1px}
.pill.orange{background:var(--orange);color:var(--ink)}
.pill.light{background:var(--white);color:var(--ink)}
.pill.dark{background:var(--ink);color:var(--white)}

.hero-title{top:166px;font:500 55px "Montserrat",sans-serif;letter-spacing:5px;color:var(--white)}
.hero-sub{top:240px;font:500 30px "Montserrat",sans-serif;letter-spacing:1px;color:var(--white)}
.hero-tag{top:308px;font:400 16px "IBM Plex Mono",monospace;letter-spacing:1px;color:var(--white)}

.step-card{top:538px;width:322px;height:189px;background:var(--ink);border-radius:16px;color:var(--white);padding:26px 25px}
.step-card h3{font:600 16px "Montserrat",sans-serif;letter-spacing:1.5px;line-height:22px;width:200px}
.step-card .num{position:absolute;right:30px;top:20px;font:700 42px "Montserrat",sans-serif;color:#4a4a4a}
.step-card p{position:absolute;left:25px;top:97px;font:400 14px "IBM Plex Mono",monospace;line-height:21px;width:275px}

.vline{width:1.5px;background:var(--line)}

.compare{left:268px;top:927px;width:662px;height:357px;border:1px solid var(--line);border-radius:18px;background:var(--white)}
.compare .row{position:absolute;left:42px;width:580px;border-bottom:1px solid #ddd;font:400 11px "IBM Plex Mono",monospace;letter-spacing:.5px}
.compare .row span{position:absolute;white-space:nowrap}
.compare .head{font:600 15px "Montserrat",sans-serif;letter-spacing:1.5px}
.c1{left:0}.c2{left:266px}.c3{left:442px}
.tick{color:var(--orange);font-style:normal}

.soon{left:83px;top:1385px;width:1034px;height:324px;background:var(--soon);border-radius:18px;overflow:hidden}
.soon-ghost{top:95px;left:0;width:1034px;text-align:center;font:800 96px "Montserrat",sans-serif;letter-spacing:8px;color:#e2e2e2}
.soon-title{top:52px;left:0;width:1034px;text-align:center;font:400 38px "Montserrat",sans-serif;letter-spacing:4px;color:var(--white)}
.soon-sub{top:124px;left:0;width:1034px;text-align:center;font:400 17px "IBM Plex Mono",monospace;letter-spacing:1px;color:var(--white)}

.perk{top:1635px;width:222px;height:149px;background:var(--ink);border-radius:14px;color:var(--white);text-align:center}
.perk svg{position:absolute;left:86px;top:33px}
.perk span{position:absolute;left:0;width:222px;top:104px;font:400 12px "IBM Plex Mono",monospace;letter-spacing:1px}

.tile{width:188px;background:var(--tile);border-radius:16px;color:var(--white);display:flex;align-items:flex-end;justify-content:center;text-align:center;padding:0 12px 26px;font:600 14px "Plus Jakarta Sans",sans-serif;line-height:22px}

.how-title{left:100px;top:2390px;font:400 42px "Montserrat",sans-serif;letter-spacing:4px}
.how-copy{left:100px;width:420px;font:400 18px "IBM Plex Mono",monospace;line-height:23px}
.how-copy b{font-weight:600}
.how-step{right:191px;text-align:right;font:400 17px "IBM Plex Mono",monospace;letter-spacing:2px;line-height:21px}
.how-dot{left:1033px}

.trust{left:0;top:2861px;width:1200px;height:333px;background:var(--ink)}
.trust-title{top:2960px;font:700 37px "Plus Jakarta Sans",sans-serif;line-height:47px;color:var(--white);letter-spacing:-.5px}
.trust-title em{font-style:normal;color:var(--orange)}
.trait{top:3126px;width:322px;height:139px;background:var(--cream);border-radius:16px;text-align:center;padding-top:36px;font:600 16px "Montserrat",sans-serif;letter-spacing:2px}
.emblem{top:3208px;width:116px;height:116px;border-radius:50%;background:#2a2a2a;border:3px solid var(--ink)}
.trusted-ghost{top:3320px;font:800 112px "Montserrat",sans-serif;letter-spacing:10px;color:#e9e9e9}
.client-name{top:3414px;font:800 46px "Plus Jakarta Sans",sans-serif;color:var(--ink)}
</style>
</head>
<body>

<div class="abs hero"></div>
<div class="abs band" style="top:624px;height:204px"></div>
<div class="abs band" style="top:1529px;height:709px"></div>

<div class="abs brand">VEYLA</div>
<a class="abs nav active" style="left:610px">HOME</a>
<a class="abs nav" style="left:685px">COMPLEMENTARY</a>
<a class="abs nav" style="left:828px">ENTERPRISE</a>
<a class="abs nav" style="left:947px">MEMBERS</a>
<div class="abs pill orange" style="left:1050px;top:25px;width:116px;height:34px">GET STARTED</div>

<h1 class="abs center-text hero-title">WELLNES FOR EVERYONE</h1>
<h2 class="abs center-text hero-sub">Modern Science Meets Ancient Wisdom</h2>
<p class="abs center-text hero-tag">Get 1-on-1 PHD Care on US for Personalized Remedies</p>
<div class="abs pill light" style="left:547px;top:368px;width:124px;height:42px">GET STARTED</div>

<div class="abs step-card" style="left:100px"><h3>TAKE TEST</h3><span class="num">01</span><p>Banh cardigan, taki thundercats forge pickl locavore mumblecore whatever sustainable vinyl.</p></div>
<div class="abs step-card" style="left:439px"><h3>GET MATCHED WITH A SPECIALIST</h3><span class="num">02</span><p>Banh cardigan, taki thundercats forge pickl locavore mumblecore whatever sustainable vinyl.</p></div>
<div class="abs step-card" style="left:778px"><h3>VIDEO CONSULT</h3><span class="num">03</span><p>Banh cardigan, taki thundercats forge pickl locavore mumblecore whatever sustainable vinyl.</p></div>

<div class="abs vline" style="left:599px;top:727px;height:200px"></div>
<div class="abs" style="left:596px;top:922px;width:8px;height:8px;border-radius:50%;background:var(--orange)"></div>
<div class="abs vline" style="left:599px;top:1284px;height:101px"></div>

<div class="abs compare">
  <div class="row head" style="top:26px;height:38px"><span class="c1">HOLLISTIC</span><span class="c2">VEYLA</span><span class="c3" style="color:var(--muted)">OTHERS</span></div>
  <div class="row" style="top:87px;height:35px"><span class="c1">QUALIFIED PHD</span><span class="c2">FREE <i class="tick">✓</i></span><span class="c3">$400 OUR OF POCKET</span></div>
  <div class="row" style="top:145px;height:35px"><span class="c1">1 ON 1</span><span class="c2">FREE <i class="tick">✓</i></span><span class="c3">$400 OUR OF POCKET</span></div>
  <div class="row" style="top:203px;height:35px"><span class="c1">PERSONALIZED</span><span class="c2">FREE <i class="tick">✓</i></span><span class="c3">WEARABLES</span></div>
  <div class="row" style="top:260px;height:35px"><span class="c1">TIME TESTED</span><span class="c2">FREE <i class="tick">✓</i></span><span class="c3">SUPPLEMENT MARKETERS</span></div>
  <div class="row" style="top:318px;height:30px;border:none"><span class="c1">WESTERN &amp; EASTERN</span><span class="c2">FREE <i class="tick">✓</i></span><span class="c3">N/A</span></div>
</div>

<div class="abs soon">
  <div class="abs soon-ghost">COMING SOON</div>
  <div class="abs soon-title">COMING SOON!</div>
  <div class="abs soon-sub">Get 1 on 1 PDH care on US for personalized remedies.</div>
  <div class="abs pill light" style="left:454px;top:172px;width:125px;height:41px">GET STARTED</div>
</div>

<div class="abs perk" style="left:131px"><svg width="50" height="50" viewBox="0 0 50 50"><circle cx="25" cy="25" r="25" fill="#f8b42c"/><path d="M15 25l7 7 13-14" fill="none" stroke="#fff" stroke-width="4" stroke-linecap="round" stroke-linejoin="round"/></svg><span>LAB TEST PARTNERS</span></div>
<div class="abs perk" style="left:369px"><svg width="50" height="50" viewBox="0 0 50 50"><circle cx="25" cy="25" r="25" fill="#f8b42c"/><path d="M15 25l7 7 13-14" fill="none" stroke="#fff" stroke-width="4" stroke-linecap="round" stroke-linejoin="round"/></svg><span>UNLIMITED CLASSES</span></div>
<div class="abs perk" style="left:608px"><svg width="50" height="50" viewBox="0 0 50 50"><circle cx="25" cy="25" r="25" fill="#f8b42c"/><path d="M15 25l7 7 13-14" fill="none" stroke="#fff" stroke-width="4" stroke-linecap="round" stroke-linejoin="round"/></svg><span>UNLIMITED YOGO</span></div>
<div class="abs perk" style="left:846px"><svg width="50" height="50" viewBox="0 0 50 50"><circle cx="25" cy="25" r="25" fill="#f8b42c"/><path d="M15 25l7 7 13-14" fill="none" stroke="#fff" stroke-width="4" stroke-linecap="round" stroke-linejoin="round"/></svg><span>UNLIMITED MEDITATION</span></div>

<div class="abs tile" style="left:100px;top:1885px;height:224px">1 On 1 With Holistic Doctors &amp; Unlimited Texting</div>
<div class="abs tile" style="left:100px;top:2127px;height:182px">Personalized Custom Supplements</div>
<div class="abs tile" style="left:303px;top:2001px;height:308px">Gut, Hormone<br>&amp; Cellular Lab Tests</div>
<div class="abs tile" style="left:507px;top:1889px;height:299px"></div>
<div class="abs pill orange" style="left:537px;top:2219px;width:125px;height:41px">GET STARTED</div>
<div class="abs tile" style="left:709px;top:2001px;height:308px">Free Yoga, Meditation &amp; Health Essentials By Star PRactitioners</div>
<div class="abs tile" style="left:912px;top:1885px;height:224px">Unlimited<br>Classes</div>
<div class="abs tile" style="left:912px;top:2127px;height:182px">Workshops</div>

<div class="abs vline" style="left:1065px;top:2309px;height:552px;background:#fbe9cc"></div>

<h2 class="abs how-title">HOW IT WORKS:</h2>
<p class="abs how-copy" style="top:2482px"><b>Sign-up</b> and get a full read of your unique constitution and what makes it thrive with a <b>custom plan made one on one with your on-demand holistic Doctor/Educator.</b></p>
<p class="abs how-copy" style="top:2621px"><b>Unlimited texting</b> to address your plan or any other concern you have about your health.</p>
<div class="abs pill dark" style="left:100px;top:2728px;width:125px;height:42px">VIEW PLANS</div>

<div class="abs how-step" style="top:2443px">Sign Up</div>
<div class="abs how-step" style="top:2564px">Get a full read<br>of your constitution</div>
<div class="abs how-step" style="top:2708px">Get a custom plan</div>
<svg class="abs how-dot" style="top:2420px" width="66" height="66" viewBox="0 0 66 66"><circle cx="33" cy="33" r="33" fill="#f8b42c"/><path d="M20 33l8 8 17-18M24 27l4 4 10-10" fill="none" stroke="#fff" stroke-width="4" stroke-linecap="round" stroke-linejoin="round"/></svg>
<svg class="abs how-dot" style="top:2552px" width="66" height="66" viewBox="0 0 66 66"><circle cx="33" cy="33" r="33" fill="#f8b42c"/><path d="M20 33l8 8 17-18M24 27l4 4 10-10" fill="none" stroke="#fff" stroke-width="4" stroke-linecap="round" stroke-linejoin="round"/></svg>
<svg class="abs how-dot" style="top:2685px" width="66" height="66" viewBox="0 0 66 66"><circle cx="33" cy="33" r="33" fill="#f8b42c"/><path d="M20 33l8 8 17-18M24 27l4 4 10-10" fill="none" stroke="#fff" stroke-width="4" stroke-linecap="round" stroke-linejoin="round"/></svg>

<div class="abs trust"></div>
<h2 class="abs center-text trust-title">Our Clients Trust Us to Provide <em>Holistic</em><br><em>Health</em> for Their Team, So Should You!</h2>

<div class="abs trait" style="left:100px">ANY CHALLENGE</div>
<div class="abs trait" style="left:439px">ANYTIME</div>
<div class="abs trait" style="left:778px">ANYWHERE</div>
<div class="abs emblem" role="img" aria-label="Circular line emblem for any challenge" style="left:203px"></div>
<div class="abs emblem" role="img" aria-label="Circular clock emblem for anytime" style="left:542px"></div>
<div class="abs emblem" role="img" aria-label="Circular globe emblem for anywhere" style="left:881px"></div>

<div class="abs center-text trusted-ghost">TRUSTED BY</div>
<div class="abs center-text client-name">Northfield Outfitters</div>

</body>
</html>
```